Brightwell Wiring Needs A Logo Design

We need a logo for my new company based out of Sacramento, Ca called Brightwell Wiring. The name says it all, my electrical contracting business provides "Brightwell Craftsman Work" I'm open to any colors that pop and customers to say Wow. I would love to print my cards on metal.

Contact Information for Business Card

The card needs to have as follows
Name of company: Brightwell Wiring
My Name: Marco Delvane
Phone # 916-555-0147
CL# 4873920
Email: brightwellwiring@mailtorva.com
and a slogan that represent "BRIGHTWELL"

Requirements
Must have
• The card needs to have as follows
• Name of company: Brightwell Wiring
• My Name : Marco Delvane
• Phone # 916-555-0147
• CL# 4873920
• Email: brightwellwiring@mailtorva.com
• and a slogan that represent "BRIGHTWELL"
Nice to have
• popping colors
• electrical Arcing

```html
<!DOCTYPE html>
<html lang="en">
<head>
<meta charset="utf-8">
<title>Brightwell Wiring – Identity and Business Cards</title>
<link href="https://fonts.googleapis.com/css2?family=Jost:wght@300;400;500;700&display=swap" rel="stylesheet">
<style>
  :root {
    --navy: #1a1050;
    --indigo: #2e2282;
    --gold: #fcd10a;
    --lemon: #f6dc16;
    --paper: #ffffff;
    --ink: #111111;
    --grey: #9a9a9a;
    --stage: #e8e3da;
  }
  * { margin: 0; padding: 0; box-sizing: border-box; }
  html, body { width: 960px; height: 1200px; overflow: hidden; }
  body { background: var(--stage); font-family: "Jost", sans-serif; position: relative; }

  .card-row { position: absolute; left: 0; width: 960px; display: flex; justify-content: center; gap: 20px; }
  .card-row--navy { top: 134px; }
  .card-row--gold { top: 836px; }

  .card { position: relative; width: 440px; height: 250px; background: var(--paper); overflow: hidden; box-shadow: 0 6px 18px rgba(0,0,0,.18); }
  .card svg { position: absolute; inset: 0; }
  .card--navy { --field: var(--indigo); --edge: var(--gold); --field-text: #ffffff; --mark: rgba(255,255,255,.13); }
  .card--gold { --field: var(--lemon); --edge: var(--indigo); --field-text: var(--indigo); --mark: rgba(40,30,110,.10); }
  .card--back { background: var(--field); }

  .card__brand { position: absolute; left: 26px; top: 96px; font-size: 21px; font-weight: 500; color: var(--indigo); white-space: nowrap; }
  .card__person { position: absolute; left: 26px; top: 136px; font-size: 14px; font-weight: 400; }
  .card__first { color: var(--gold); }
  .card__last { color: var(--indigo); }
  .card__role { display: block; font-size: 10px; color: var(--grey); margin-top: 2px; letter-spacing: .5px; }

  .card__contact { position: absolute; right: 18px; top: 66px; text-align: right; font-size: 10.5px; line-height: 1.7; color: var(--field-text); font-weight: 400; white-space: nowrap; }
  .card__slogan { position: absolute; right: 14px; bottom: 12px; font-size: 16px; font-weight: 500; color: var(--mark); letter-spacing: 1px; white-space: nowrap; }
  .card__slogan--back { right: auto; left: 24px; bottom: auto; top: 24px; font-size: 40px; }

  .brand-band { position: absolute; top: 518px; left: 0; width: 960px; height: 204px; display: flex; }
  .brand-band__half { width: 480px; height: 204px; display: flex; align-items: center; justify-content: center; }
  .brand-band__half--navy { background: var(--navy); color: #ffffff; }
  .brand-band__half--gold { background: var(--gold); color: var(--ink); }
  .brand-band__name { font-size: 42px; font-weight: 500; letter-spacing: .5px; }
</style>
</head>
<body>

  <section class="card-row card-row--navy">
    <article class="card card--navy">
      <svg width="440" height="250" viewBox="0 0 440 250" aria-hidden="true">
        <polygon points="262,0 440,0 440,250 210,250" fill="var(--field)"/>
        <line x1="262" y1="0" x2="210" y2="250" stroke="var(--edge)" stroke-width="4"/>
      </svg>
      <p class="card__brand">Brightwell Wiring</p>
      <p class="card__person"><span class="card__first">Marco</span> <span class="card__last">Delvane</span><span class="card__role">owner</span></p>
      <p class="card__contact">Phone : 916-555-0147<br>CL: 4873920<br>Email:<br>brightwellwiring@mailtorva.com</p>
      <p class="card__slogan">BRIGHTWELL SERVICES</p>
    </article>
    <article class="card card--navy card--back">
      <svg width="440" height="250" viewBox="0 0 440 250" aria-hidden="true">
        <polygon points="440,110 440,250 250,250" fill="var(--paper)"/>
        <line x1="440" y1="110" x2="250" y2="250" stroke="var(--edge)" stroke-width="4"/>
      </svg>
      <p class="card__slogan card__slogan--back">BRIGHTWELL</p>
    </article>
  </section>

  <section class="brand-band">
    <div class="brand-band__half brand-band__half--navy"><p class="brand-band__name">Brightwell Wiring</p></div>
    <div class="brand-band__half brand-band__half--gold"><p class="brand-band__name">Brightwell Wiring</p></div>
  </section>

  <section class="card-row card-row--gold">
    <article class="card card--gold">
      <svg width="440" height="250" viewBox="0 0 440 250" aria-hidden="true">
        <polygon points="262,0 440,0 440,250 210,250" fill="var(--field)"/>
        <line x1="262" y1="0" x2="210" y2="250" stroke="var(--edge)" stroke-width="4"/>
      </svg>
      <p class="card__brand">Brightwell Wiring</p>
      <p class="card__person"><span class="card__first">Marco</span> <span class="card__last">Delvane</span><span class="card__role">owner</span></p>
      <p class="card__contact">Phone : 916-555-0147<br>CL: 4873920<br>Email:<br>brightwellwiring@mailtorva.com</p>
      <p class="card__slogan">BRIGHTWELL SERVICES</p>
    </article>
    <article class="card card--gold card--back">
      <svg width="440" height="250" viewBox="0 0 440 250" aria-hidden="true">
        <polygon points="440,110 440,250 250,250" fill="var(--paper)"/>
        <line x1="440" y1="110" x2="250" y2="250" stroke="var(--edge)" stroke-width="4"/>
      </svg>
      <p class="card__slogan card__slogan--back">BRIGHTWELL</p>
    </article>
  </section>

</body>
</html>
```